We are growing our coaching practice and need some help creating collateral

Our organisation is building a coaching practice. It's going well and we want to take it to the next level. To date, we've done our own basic marketing material (attached), but now we want to create something more substantial that captures our approach and gives us confidence and pride when talking to customers. Things to note - we aren't looking for logo design, that's a separate branding discussion in our organisation. We are looking for someone to take our existing content and make it look good - this might be in the form of a flyer or PPT slide deck for example.
The format we are looking for is the offering title - in this case, 'Coaching', a brief description, and then some further detail.
Target Market(s)
Corporate, Healthcare, IT
Colors
Designer to choose colors to be used in the design.
Look and feel
Each slider illustrates characteristics of the customer's brand and the style your logo design should communicate.

```html
<!DOCTYPE html>
<html lang="en">
<head>
<meta charset="utf-8">
<title>Coaching flyer</title>
<link rel="stylesheet" href="https://fonts.googleapis.com/css2?family=Raleway:wght@300;400&family=Tinos:wght@400&display=swap">
<style>
  :root {
    --backdrop: #eef3f7;
    --paper: #ffffff;
    --ink: #1c1c1c;
    --accent: #2f9bd6;
    --tint: #e3f0fa;
    --panel: rgba(120, 190, 235, 0.45);
    --hero-top: #5fa6e0;
    --hero-bottom: #8fb85a;
  }
  * { box-sizing: border-box; margin: 0; padding: 0; }
  html, body {
    width: 1200px; height: 1200px; overflow: hidden;
    background: var(--backdrop);
  }
  .flyer {
    position: absolute; left: 180px; top: 70px;
    width: 840px; height: 1060px;
    background: var(--paper);
    box-shadow: 0 6px 24px rgba(0,0,0,0.12);
    overflow: hidden;
    font-family: "Tinos", "Times New Roman", serif;
    color: var(--ink);
  }
  .flyer__tint { position: absolute; inset: 0; }
  .hero {
    position: absolute; left: 0; top: 0; width: 840px; height: 312px;
  }
  .hero__photo {
    position: absolute; inset: 0;
    background: linear-gradient(180deg, var(--hero-top) 0%, var(--hero-bottom) 100%);
  }
  .hero__panel {
    position: absolute; left: 65px; top: 0; width: 290px; height: 312px;
    background: var(--panel);
    padding: 28px 16px 0 16px;
    color: #fff;
  }
  .hero__title {
    font-family: "Raleway", Arial, sans-serif; font-weight: 300;
    font-size: 60px; line-height: 1; letter-spacing: 0.5px;
    text-align: center;
  }
  .hero__web {
    font-size: 14px; text-align: center; margin-top: 2px;
  }
  .hero__intro {
    font-size: 12.5px; line-height: 1.45; margin-top: 22px;
  }
  .overview {
    position: absolute; left: 80px; top: 332px; width: 730px;
    font-size: 12.6px; line-height: 1.5;
  }
  .overview p { text-align: justify; }
  .section-title {
    font-family: "Raleway", Arial, sans-serif; font-weight: 300;
    color: var(--accent); font-size: 30px; line-height: 1.12;
  }
  .coach {
    position: absolute; left: 80px; top: 538px; width: 370px;
    font-size: 12.6px; line-height: 1.5;
  }
  .coach .section-title { margin-bottom: 8px; }
  .coach p { text-align: justify; }
  .credentials {
    position: absolute; left: 476px; top: 538px; width: 330px;
    font-size: 12.6px; line-height: 1.5;
  }
  .credentials .section-title { margin-bottom: 14px; }
  .credentials ul { list-style: none; }
</style>
</head>
<body>
  <main class="flyer">
    <svg class="flyer__tint" width="840" height="1060" viewBox="0 0 840 1060" aria-hidden="true">
      <polygon points="0,600 0,1060 220,1060" fill="var(--tint)"/>
      <polygon points="840,380 840,1060 560,1060 520,700" fill="var(--tint)" opacity="0.55"/>
    </svg>

    <header class="hero">
      <div class="hero__photo" role="img" aria-label="Photo of a sunlit green park with trees under a blue sky"></div>
      <div class="hero__panel">
        <h1 class="hero__title">Coaching</h1>
        <p class="hero__web">www.meridiancoaching.com</p>
        <p class="hero__intro">We believe great coaching is a bridge, one that enables you to see more clearly and grow the unexpected chance; one that supports and challenges your thinking and actions to support your identified goals. We build a creative and confidential partnership with you, one that is grounded in the science of leadership, change and coaching psychology so that practical results are an expectation and not left to chance.</p>
      </div>
    </header>

    <section class="overview">
      <p>Our coaches are highly attuned to the human systems within which you work and live, since understanding those interconnected forces is vital to unlock movement. We build on your existing strengths and seek sustainable shifts, ones that create ripple effects of positive change.</p>
      <p>Leaders everywhere face unprecedented change, pressure, ambiguity, culture and accountability dilemmas. And yet every leader also has a different story, different terrain to navigate and different aspirations. This is where executive coaching with MCP can create extraordinary results Our coaching packages typically consist of blocks of 7 hourly sessions, conducted fortnightly (with flexibility to customise).</p>
      <p>For EL2 leaders, the investment in a block of 7 sessions is $3400 + GST. This includes significant preparation and conceptualisation time before and after sessions by your coach to ensure you achieve maximum value. Why not explore the possibilities executive coaching offers through a no obligation initial session, ensuring the approach and the coach is a good fit for you? Contact Sam Porter, ph. 0400 000 000, sam.porter@meridiancoaching.com</p>
    </section>

    <section class="coach">
      <h2 class="section-title">Meet one of our Coaches</h2>
      <p>Sam Porter leads the Executive Coaching practice for MCP across Australia and New Zealand.</p>
      <p>He has worked at senior levels in the ACT Public Service, the Australian Public Service and in the private sector. His continuing focus over the past 20 years has been on organisational and people development. As a Masters-qualified and highly experienced executive coach, Sam's passion lies in unlocking human potential. He has coached doctors, nurses, allied health clinicians, statisticians, scientists, educators, IT professionals, Senior managers and Executives in the APS (EL1 – SES), ACT Government (SOGC – Executive bands) and private sector.</p>
      <p>When Sam is not coaching, he is facilitating workshops and consulting to enable teams and organisations to make effective transformations.</p>
    </section>

    <section class="credentials">
      <h2 class="section-title">Qualifications,<br>Accreditations,<br>Memberships</h2>
      <ul>
        <li>Master of Science in Coaching Psychology</li>
        <li>Graduate Certificate in Management</li>
        <li>Certificate IV in Workplace Assessment &amp; Training</li>
        <li>Culture Profile Accreditation, Culture Dynamics</li>
        <li>Type Profile Accreditation</li>
        <li>Member, Global Coaching Federation (GCF)</li>
        <li>Member, Harbour University Coaching &amp; Mentoring Alumni Association</li>
      </ul>
    </section>
  </main>
</body>
</html>
```